Need a website to promote and sell my book

Using images from the book, I need a website designed that helps promote the book and eventually sell it.
*Need a landing page
*About the author page
*Storefront page to purchase
*Coming soon page
*"Featured in" page that can link to news articles etc.
The images posted here are examples, the winner of the contest will get the images from the finished book. I will provide the exact text to the winner of the contest.

I can also provide images of kids reading the book. For now, I'll just use one, the winner can have them all to choose from.
Updates

Extending deadline to allow for a few more designers to submit and to allow time for me to review and hold a poll

Target Market(s)

Parents, aunts, uncles, grandparents, friends who have kids; teachers, daycare teachers, babysitters etc.

Industry/Entity Type

Custom Publishing

Coding

Coded - Design and coding required

Number of Pages Required

5+ page

Font styles to use
Sans Serif

Colors

Designer to choose colors to be used in the design.

Requirements
Must have
• It must have a fun feel like the book.
Nice to have
• Would be great to have a section that automatically pulls tweets about the book into it.

```html
<!DOCTYPE html>
<html lang="en">
<head>
<meta charset="utf-8">
<title>Let's Play with Chemistry</title>
<link href="https://fonts.googleapis.com/css2?family=Amatic+SC:wght@700&family=Bebas+Neue&family=Poppins:wght@400;500;600;700&display=swap" rel="stylesheet">
<style>
:root{
  --red:#e14a46;
  --red-dark:#d63c38;
  --yellow:#fdc23c;
  --blue:#6fc4e2;
  --grey:#f0f0f0;
  --ink:#222;
  --dark:#232323;
  --darker:#1b1b1b;
  --white:#fff;
  --orange:#f99a3a;
  --sky:#3ec6f3;
}
*{margin:0;padding:0;box-sizing:border-box}
html,body{width:1200px;height:2548px;overflow:hidden}
body{position:relative;background:var(--grey);font-family:'Poppins',sans-serif;color:var(--ink)}
.abs{position:absolute}
.hand{font-family:'Amatic SC',sans-serif;font-weight:700}
.pill{position:absolute;display:flex;align-items:center;justify-content:center;gap:22px;border-radius:24px;font-size:17px}

/* header */
.site-header{position:absolute;left:0;top:0;width:1200px;height:65px;background:var(--white)}
.logo{position:absolute;left:94px;top:14px;line-height:1}
.logo b{display:block;font-size:22px;font-weight:700;letter-spacing:-.5px}
.logo span{display:block;font-size:12px;margin-top:2px}
.main-nav{position:absolute;left:298px;top:26px;display:flex;font-size:13px}
.main-nav a{color:var(--ink);text-decoration:none;margin-right:36px}
.main-nav a.active{color:var(--red);border-bottom:2px solid var(--red);padding-bottom:4px}
.cart{position:absolute;left:813px;top:18px;width:33px;height:33px;border-radius:50%;background:var(--red-dark)}

/* hero */
.hero-title{position:absolute;left:110px;top:128px;color:var(--white);line-height:1;text-shadow:3px 3px 0 rgba(150,30,30,.35)}
.hero-title .l1{font-size:104px;display:block}
.hero-title .l2{font-size:150px;display:block;margin-top:-18px;letter-spacing:3px}
.hero-by{position:absolute;left:125px;top:378px;color:var(--white);font-size:24px;font-weight:500}
.btn-read{left:118px;top:440px;width:188px;height:43px;background:var(--blue);color:#2a3d4d;font-family:'Bebas Neue',sans-serif;font-size:22px}
.btn-buy{left:318px;top:440px;width:188px;height:43px;background:var(--yellow);color:#2a2a2a;font-family:'Bebas Neue',sans-serif;font-size:22px}

/* about */
.about-label{position:absolute;left:637px;top:725px;font-size:18px;font-weight:500}
.about-name{position:absolute;left:633px;top:755px;font-size:58px;color:var(--red);line-height:1;white-space:nowrap}
.about-text{position:absolute;left:636px;top:836px;width:346px;font-size:11.3px;line-height:21px;text-align:justify;color:#333}
.btn-about{left:628px;top:980px;width:186px;height:42px;background:var(--yellow);color:#333}

/* coming soon */
.soon-title{position:absolute;left:684px;top:1260px;font-size:80px;color:var(--white);line-height:1;white-space:nowrap}
.soon-text{position:absolute;left:683px;top:1358px;width:306px;font-size:14px;line-height:23px;color:var(--white)}
.btn-soon{left:690px;top:1496px;width:186px;height:43px;background:var(--yellow);color:#333}

/* featured */
.featured{position:absolute;left:0;top:1632px;width:1200px;height:532px;background:linear-gradient(#e4e4e4,#fff 120px)}
.featured h2{position:absolute;width:1200px;top:104px;text-align:center;font-size:50px;line-height:1;color:var(--red)}
.featured .rule{position:absolute;left:584px;top:163px;width:30px;height:2px;background:var(--yellow)}
.card{position:absolute;top:192px;width:222px;text-align:center}
.card .art{position:relative;width:222px;height:183px}
.card .date{position:absolute;left:15px;top:15px;width:46px;height:46px;border-radius:50%;background:var(--yellow);font-family:Georgia,serif;color:#222;line-height:1;padding-top:8px;font-size:15px}
.card .date small{display:block;font-size:8px}
.card .cat{margin-top:15px;font-size:7.5px;color:var(--red);text-transform:uppercase}
.card .title{margin-top:10px;font-size:8.6px;line-height:18px;font-weight:600;text-transform:uppercase}
.card .more{display:inline-block;margin-top:10px;border:1.5px solid var(--yellow);border-radius:12px;padding:3px 11px;font-size:7.5px;font-weight:600}

/* footer */
.site-footer{position:absolute;left:0;top:2164px;width:1200px;height:384px;background:var(--dark);color:var(--white)}
.foot-logo{position:absolute;width:1200px;top:55px;text-align:center;line-height:1}
.foot-logo b{display:block;font-size:38px;font-weight:700}
.foot-logo span{display:block;font-size:22px}
.contact{position:absolute;top:176px;display:flex;align-items:center;gap:14px}
.contact .ico{width:49px;height:49px;border-radius:50%;background:var(--yellow)}
.contact h4{color:var(--red);font-weight:500;font-size:15px}
.contact p{font-size:12px;margin-top:3px}
.divider{position:absolute;top:148px;width:1px;height:76px;background:#fff}
.foot-bottom{position:absolute;left:0;top:254px;width:1200px;height:130px;background:var(--darker)}
.social{position:absolute;left:538px;top:19px;display:flex;gap:8px}
.social i{width:25px;height:25px;border-radius:50%;background:#3c3c3c;display:block}
.foot-nav{position:absolute;width:1200px;top:62px;display:flex;justify-content:center;gap:33px;font-size:13px;font-weight:500}
.copy{position:absolute;width:1200px;top:100px;text-align:center;font-size:9px;color:#666}
</style>
</head>
<body>

<svg width="0" height="0" style="position:absolute">
  <defs>
    <linearGradient id="coverSky" x1="0" y1="0" x2="0" y2="1">
      <stop offset="0" stop-color="#62c0e6"/>
      <stop offset=".45" stop-color="#8fd3ea"/>
      <stop offset=".62" stop-color="#c9b08a"/>
      <stop offset=".78" stop-color="#f0c06a"/>
      <stop offset="1" stop-color="#f7b552"/>
    </linearGradient>
    <radialGradient id="coverGlow" cx=".55" cy=".35" r=".45">
      <stop offset="0" stop-color="#fdf6e6" stop-opacity=".85"/>
      <stop offset="1" stop-color="#fdf6e6" stop-opacity="0"/>
    </radialGradient>
    <radialGradient id="coverWarm" cx=".5" cy=".72" r=".4">
      <stop offset="0" stop-color="#e8785a" stop-opacity=".55"/>
      <stop offset="1" stop-color="#e8785a" stop-opacity="0"/>
    </radialGradient>
    <linearGradient id="spine" x1="0" y1="0" x2="1" y2="0">
      <stop offset="0" stop-color="#3ea4cc"/>
      <stop offset="1" stop-color="#6cc6e4"/>
    </linearGradient>
  </defs>
</svg>

<!-- hero background shapes -->
<svg class="abs" style="left:0;top:0" width="1200" height="680" viewBox="0 0 1200 680">
  <defs>
    <radialGradient id="heroRed" cx=".3" cy=".4" r=".8">
      <stop offset="0" stop-color="#e8544f"/>
      <stop offset="1" stop-color="#dc423e"/>
    </radialGradient>
  </defs>
  <path d="M880 0 H1200 V548 C1010 552 860 640 600 645 C430 640 360 580 300 548 V400 L880 0Z" fill="var(--yellow)"/>
  <path d="M0 65 H935 C820 170 700 330 610 545 C460 548 240 545 0 545Z" fill="url(#heroRed)"/>
  <path d="M0 552 C240 552 380 645 600 650 C820 645 960 552 1200 548" fill="none" stroke="var(--red)" stroke-width="8"/>
  <circle cx="599" cy="598" r="17" fill="none" stroke="#fff" stroke-width="2.5"/>
  <path d="M599 588 V606 M592 600 L599 607 L606 600" fill="none" stroke="#fff" stroke-width="2.5" stroke-linecap="round" stroke-linejoin="round"/>
</svg>

<header class="site-header">
  <div class="logo"><b>LOGO HERE</b><span>TAGLINE GOES HERE</span></div>
  <nav class="main-nav">
    <a class="active">Home</a><a>About Us</a><a>Coming Soon</a><a>Features</a><a>Contact</a>
  </nav>
  <div class="cart"><svg width="33" height="33" viewBox="0 0 33 33"><path d="M10 14 H23 L21.5 23 H11.5Z M13 14 L16.5 9 L20 14" fill="none" stroke="#fff" stroke-width="1.8" stroke-linejoin="round"/></svg></div>
</header>

<div class="hero-title hand"><span class="l1">Let's Play with</span><span class="l2">CHEMISTRY</span></div>
<div class="hero-by">Written by: Margaret Ellison, Phd</div>
<div class="pill btn-read">READ MORE <svg width="24" height="24" viewBox="0 0 24 24"><circle cx="12" cy="12" r="10" fill="none" stroke="#2a3d4d" stroke-width="1.6"/><path d="M9 8 L13 12 L9 16 M12 8 L16 12 L12 16" fill="none" stroke="#2a3d4d" stroke-width="1.6"/></svg></div>
<div class="pill btn-buy">BUY NOW <svg width="18" height="22" viewBox="0 0 18 22"><rect x="2" y="6" width="14" height="14" rx="2" fill="none" stroke="#2a2a2a" stroke-width="1.6"/><path d="M6 6 V4 A3 3 0 0 1 12 4 V6" fill="none" stroke="#2a2a2a" stroke-width="1.6"/></svg></div>

<svg class="abs" style="left:560px;top:60px" width="600" height="510" viewBox="0 0 600 510" role="img" aria-label="Book cover illustration of children reading among colourful chemistry flasks, atoms and a microscope">
  <path d="M75 495 L560 400 L575 410 L90 505Z" fill="#000" opacity=".18"/>
  <path d="M55 45 L560 10 L562 400 L70 490Z" fill="#f4f1ea"/>
  <path d="M45 50 L550 12 L550 395 L60 490Z" fill="url(#coverSky)"/>
  <path d="M45 50 L550 12 L550 395 L60 490Z" fill="url(#coverGlow)"/>
  <path d="M45 50 L550 12 L550 395 L60 490Z" fill="url(#coverWarm)"/>
  <path d="M45 50 L72 54 L86 486 L60 490Z" fill="url(#spine)"/>
</svg>

<!-- about -->
<svg class="abs" style="left:220px;top:680px" width="385" height="395" viewBox="0 0 385 395">
  <circle cx="187" cy="195" r="187" fill="none" stroke="#222" stroke-width="1.5"/>
</svg>
<div class="abs" role="img" aria-label="Portrait photo of the smiling author" style="left:251px;top:710px;width:312px;height:312px;border-radius:50%;background:radial-gradient(circle at 42% 42%,#e6c6ad 0,#c9a38a 22%,#9aa3ab 55%,#6f8196 80%,#58687a)"></div>
<svg class="abs" style="left:428px;top:893px" width="176" height="170" viewBox="0 0 176 170" role="img" aria-label="Book cover held by the author">
  <path d="M10 160 L170 140 L172 146 L14 166Z" fill="#000" opacity=".15"/>
  <path d="M8 20 L170 4 L170 138 L14 162Z" fill="#f4f1ea"/>
  <path d="M4 22 L166 6 L166 136 L10 162Z" fill="url(#coverSky)"/>
  <path d="M4 22 L166 6 L166 136 L10 162Z" fill="url(#coverGlow)"/>
  <path d="M4 22 L12 23 L18 161 L10 162Z" fill="url(#spine)"/>
</svg>
<div class="about-label">ABOUT THE AUTHOR</div>
<div class="about-name hand">MARGARET ELLISON PHD</div>
<p class="about-text">Lorem ipsum dolor sit amet, consectetur adipiscing elit, sed do eiusmod tempor incididunt ut labore et dolore magna aliqua. Ut enim ad minim veniam, quis nostrud exercitation ullamco laboris nisi ut aliquip ex ea commodo consequat. Duis aute irure dolor in reprehenderit in voluptate velit esse cillum dolore eu fugiat nulla pariatur.</p>
<div class="pill btn-about">READ MORE <svg width="18" height="16" viewBox="0 0 18 16"><path d="M3 2 L9 8 L3 14 M9 2 L15 8 L9 14" fill="none" stroke="#333" stroke-width="2.2"/></svg></div>

<!-- coming soon -->
<svg class="abs" style="left:0;top:1090px" width="1200" height="545" viewBox="0 0 1200 545">
  <defs>
    <radialGradient id="soonRed" cx=".3" cy=".5" r=".8">
      <stop offset="0" stop-color="#e8544f"/>
      <stop offset="1" stop-color="#dc423e"/>
    </radialGradient>
  </defs>
  <rect x="0" y="109" width="1200" height="436" fill="url(#soonRed)"/>
  <path d="M0 100 C230 100 380 12 600 10 C820 12 970 100 1200 100" fill="none" stroke="var(--red)" stroke-width="7"/>
  <circle cx="599" cy="75" r="20" fill="none" stroke="#fff" stroke-width="2.5"/>
  <path d="M599 64 V85 M591 78 L599 86 L607 78" fill="none" stroke="#fff" stroke-width="2.5" stroke-linecap="round" stroke-linejoin="round"/>
</svg>
<svg class="abs" style="left:140px;top:1218px" width="520" height="370" viewBox="0 0 520 370" role="img" aria-label="Printed book and tablet showing the colourful cover with children and chemistry items">
  <path d="M25 362 L400 305 L410 312 L32 370Z" fill="#000" opacity=".18"/>
  <path d="M12 33 L400 4 L402 302 L26 358Z" fill="#f4f1ea"/>
  <path d="M5 36 L394 7 L394 300 L20 360Z" fill="url(#coverSky)"/>
  <path d="M5 36 L394 7 L394 300 L20 360Z" fill="url(#coverGlow)"/>
  <path d="M5 36 L394 7 L394 300 L20 360Z" fill="url(#coverWarm)"/>
  <path d="M5 36 L18 38 L28 358 L20 360Z" fill="url(#spine)"/>
  <rect x="262" y="176" width="248" height="172" rx="12" fill="#000" opacity=".15"/>
  <rect x="258" y="170" width="248" height="172" rx="12" fill="#fff"/>
  <rect x="282" y="182" width="200" height="148" fill="url(#coverSky)"/>
  <rect x="282" y="182" width="200" height="148" fill="url(#coverGlow)"/>
  <circle cx="270" cy="256" r="4" fill="none" stroke="#bbb"/>
</svg>
<div class="soon-title hand">COMING SOON</div>
<p class="soon-text">"Lorem ipsum dolor sit amet, consectetur adipiscing elit, sed do eiusmod tempor incididunt ut labore et dolore magna aliqua. Ut enim ad minim veniam, quis nostrud exercitation ullamco laboris .</p>
<div class="pill btn-soon">BUY NOW <svg width="18" height="22" viewBox="0 0 18 22"><rect x="2" y="6" width="14" height="14" rx="2" fill="none" stroke="#333" stroke-width="1.6"/><path d="M6 6 V4 A3 3 0 0 1 12 4 V6" fill="none" stroke="#333" stroke-width="1.6"/></svg></div>

<!-- featured -->
<section class="featured">
  <h2 class="hand">FEATURED IN</h2>
  <div class="rule"></div>
  <article class="card" style="left:221px">
    <div class="art" role="img" aria-label="Illustration of a child with a ball and the text I had fun learning about chemistry today" style="background:radial-gradient(circle at 60% 45%,#ffc36a,#f99a3a 60%,#f18a2c)"><div class="date">25<small>April</small></div></div>
    <div class="cat">Clients, Case-Study</div>
    <div class="title">Lorem ipsum dolor sit amet, consectetur<br>adipiscing elit, sed do eiusmod tempor.</div>
    <span class="more">READ MORE</span>
  </article>
  <article class="card" style="left:490px">
    <div class="art" role="img" aria-label="Illustration of a child with a microscope and the text learned about chemistry today" style="background:radial-gradient(circle at 60% 50%,#f3a04a,#e14a46 60%,#d63c38)"><div class="date">25<small>April</small></div></div>
    <div class="cat">Clients, Case-Study</div>
    <div class="title">Lorem ipsum dolor sit amet, consectetur<br>adipiscing elit, sed do eiusmod tempor.</div>
    <span class="more">READ MORE</span>
  </article>
  <article class="card" style="left:757px">
    <div class="art" role="img" aria-label="Illustration of a child with the text I had fun learning about chemistry today" style="background:radial-gradient(circle at 55% 50%,#8fe0fb,#3ec6f3 60%,#2cb8ea)"><div class="date">25<small>April</small></div></div>
    <div class="cat">Clients, Case-Study</div>
    <div class="title">Lorem ipsum dolor sit amet, consectetur<br>adipiscing elit, sed do eiusmod tempor.</div>
    <span class="more">READ MORE</span>
  </article>
</section>

<!-- footer -->
<footer class="site-footer">
  <div class="foot-logo"><b>LOGO HERE</b><span>TAGLINE GOES HERE</span></div>
  <div class="contact" style="left:222px">
    <div class="ico"><svg width="49" height="49" viewBox="0 0 49 49"><path d="M17 16 C15 20 20 30 30 33 L33 30 L29 27 L27 29 C24 28 21 25 20 22 L22 20 L19 16Z" fill="#222"/></svg></div>
    <div><h4>Phone Number</h4><p>123-4567-8901</p></div>
  </div>
  <div class="divider" style="left:452px"></div>
  <div class="contact" style="left:510px">
    <div class="ico"><svg width="49" height="49" viewBox="0 0 49 49"><rect x="13" y="16" width="23" height="17" rx="2" fill="#222"/><path d="M14 18 L24.5 26 L35 18" fill="none" stroke="#fdc23c" stroke-width="2"/></svg></div>
    <div><h4>Email Address</h4><p>info@bookmail.com</p></div>
  </div>
  <div class="divider" style="left:723px"></div>
  <div class="contact" style="left:775px">
    <div class="ico"><svg width="49" height="49" viewBox="0 0 49 49"><path d="M24.5 36 C18 28 16 24 16 21 A8.5 8.5 0 0 1 33 21 C33 24 31 28 24.5 36Z" fill="none" stroke="#222" stroke-width="2.2"/><circle cx="24.5" cy="21" r="3" fill="#222"/></svg></div>
    <div><h4>Location</h4><p>Lorem ipsum street, 2345</p></div>
  </div>
  <div class="foot-bottom">
    <div class="social"><i></i><i></i><i></i><i></i></div>
    <nav class="foot-nav"><span>Home</span><span>About Us</span><span>Coming Soon</span><span>Features</span><span>Contact</span></nav>
    <div class="copy">Copyright © 2019 Company. All Rights Reserved. Privacy Policy</div>
  </div>
</footer>

</body>
</html>
```